Thought Harbor Tri-Fold Brochure - Recovering From Alzheimer's

Design a brochure a brochure for Thought Harbor. www.thoughtharbor.org. We help people with Alzheimer's, or who have had a Traumatic Brain Injury, Concussion or Stroke stop their cognitive decline, and actually reverse decline and improve their cognitive abilities. We use an individualized approach, utilizing extensive lab work and developing a roadmap that includes diet, supplementation, theraputic devices all guided by a Memory Coach. I would like to see a design with pictures of people similar to the demographic on the website. Also incorporate some of the colors from my logo. We offer hope to people who consistently hear, "There is nothing we can do. Alzheimer's is a fatal disease." NOT TRUE! We see people's lives change every day!!!!

Target Market(s)

People who ARE or know someone suffering from cognitive decline, Alzheimer's, Traumatic Brain Injury, Concussion or Stroke.

Industry/Entity Type

Health and wellbeing -- Treating Alzheimer's.

Font styles to use
Other font styles liked:
• Calibri or I think it's called Lota

Colors
0054AA
0677BA
7BADD7
CADEEF
E8F1F8
0094D4
00A9DD
6FCCEA
C7EBF8
E9F6FB
00AB8E
00BBA5
67D7C9
C6EFE9
E9F9F6

Requirements
Must have
• Easily read material (think older eyes) and people between the ages of 40-70. Needs to have a professional feel but not clinical. Create trust and a feeling of caring and hope.
Nice to have
• Please check out my website: www.thoughtharbor.org for content and feel.
Should not have
• Youthful people exercising OR highly stereotypical ageist photos or info.

```html
<!DOCTYPE html>
<html lang="en">
<head>
<meta charset="utf-8">
<title>Thought Harbor Tri-Fold Brochure</title>
<link href="https://fonts.googleapis.com/css2?family=Open+Sans:ital,wght@0,400;0,600;0,700;0,800;1,400&display=swap" rel="stylesheet">
<style>
:root{
  --green:#1f9a3c;
  --blue:#0a67b5;
  --ink:#1d1d1d;
  --paper:#ffffff;
  --stage:#d8d9da;
  --photo-warm:#c9a57e;
  --photo-cool:#9fb0c2;
  --photo-flower:#b7b58a;
}
*{box-sizing:border-box;margin:0;padding:0}
html,body{width:1200px;height:2229px;overflow:hidden}
body{background:var(--stage);font-family:"Open Sans",Arial,sans-serif;color:var(--ink);position:relative}
.spread{position:absolute;left:40px;width:1120px;height:860px;background:var(--paper);box-shadow:0 10px 30px rgba(0,0,0,.18);overflow:hidden}
.spread--outside{top:200px}
.spread--inside{top:1140px}
.spread-art{position:absolute;inset:0}
.abs{position:absolute}
.photo{position:absolute;border-radius:50%;border:7px solid var(--blue);overflow:hidden}
.photo-fill{width:100%;height:100%}
.brand{position:absolute;display:flex;align-items:center;gap:10px;font-weight:700;color:var(--blue);letter-spacing:.5px;text-transform:uppercase}
.brand-dot{border-radius:50%;background:var(--green);flex:none}
.brand--light{color:#fff}
.brand--light .brand-dot{background:#fff}
.heading{font-weight:800;color:var(--blue);text-transform:uppercase;line-height:1.05}
.body-copy{font-size:12px;line-height:1.5;text-align:justify}
.body-copy p+p{margin-top:9px}
/* outside */
.services{left:28px;top:245px;width:330px}
.services .heading{font-size:26px}
.services .tagline{font-size:18px;margin:6px 0 10px}
.services .body-copy{font-size:11.5px;line-height:1.45;font-style:italic}
.back-url{left:30px;bottom:24px;color:#fff;font-size:13px}
.revolution{left:400px;top:40px;width:330px}
.revolution .heading{font-size:28px}
.checklist{list-style:none;margin:14px 0 12px}
.checklist li{display:flex;align-items:center;gap:8px;font-size:13.5px;margin-bottom:5px}
.checklist li::before{content:"";width:12px;height:12px;border-radius:50%;background:var(--blue);box-shadow:inset 0 0 0 3px #7badd7;flex:none}
.strategies{font-weight:800;font-size:13.5px;text-transform:uppercase;line-height:1.3}
.slogan{margin-top:18px;font-weight:800;color:var(--green);font-size:25px;line-height:1.1;text-transform:uppercase}
.contact-title{margin-top:18px;font-size:24px;font-weight:800}
.contact-list{list-style:none;margin-top:10px}
.contact-list li{display:flex;align-items:center;gap:12px;font-size:13.5px;margin-bottom:8px}
.contact-icon{width:26px;height:26px;flex:none}
.cover-title{left:785px;top:575px;width:320px;color:#fff;font-weight:800;font-size:48px;line-height:.98;text-transform:uppercase;text-align:center}
.cover-pill{left:810px;top:750px;width:270px;height:38px;border-radius:19px;background:var(--blue);color:#fff;font-weight:700;font-size:17px;display:flex;align-items:center;justify-content:center}
/* inside */
.testimonials{left:28px;top:400px;width:330px}
.testimonials .heading{font-size:26px;padding-bottom:6px;border-bottom:2px solid var(--green);display:inline-block}
.quote{margin-top:16px}
.quote-name{display:flex;align-items:center;gap:8px;color:var(--green);font-weight:800;font-size:14px;margin-bottom:6px}
.quote-name svg{width:24px;height:24px;flex:none}
.approach{left:400px;top:70px;width:325px}
.approach .heading{font-size:28px}
.approach .sub{font-weight:700;font-size:16px;margin:12px 0 10px}
.team{left:773px;top:60px;width:275px}
.team .heading{font-size:28px}
.member{display:flex;align-items:center;gap:14px;margin-top:26px}
.member-photo{width:86px;height:86px;border-radius:50%;border:5px solid var(--blue);flex:none;background:linear-gradient(160deg,#8fa6bd,#3c4a5c)}
.member-name{color:var(--blue);font-weight:800;font-size:15px}
.member-role{font-size:12.5px;line-height:1.35}
.inside-url{right:40px;bottom:36px;color:#fff;font-size:14px}
</style>
</head>
<body>

<section class="spread spread--outside">
  <svg class="spread-art" viewBox="0 0 1120 860" aria-hidden="true">
    <path d="M0 0 L260 0 C190 40 90 70 0 120 Z" fill="var(--green)"/>
    <path d="M0 132 C90 80 190 48 270 6" stroke="var(--blue)" stroke-width="8" fill="none"/>
    <path d="M0 592 C60 576 140 590 200 622 C120 620 60 626 0 636 Z" fill="var(--blue)"/>
    <path d="M1120 230 L1120 480 C1060 470 990 490 940 520 C1010 430 1070 330 1120 230 Z" fill="var(--blue)"/>
    <path d="M0 645 C200 585 420 690 600 645 C700 615 760 545 820 505 C900 455 1000 400 1120 340 L1120 860 L0 860 Z" fill="var(--green)"/>
    <path d="M280 660 C420 700 540 680 620 640 C720 590 790 520 870 478 C950 438 1040 388 1120 340" stroke="var(--blue)" stroke-width="9" fill="none"/>
    <path d="M560 672 C650 660 710 620 770 565" stroke="#fff" stroke-width="5" fill="none"/>
  </svg>

  <div class="photo" style="left:165px;top:45px;width:190px;height:190px">
    <div class="photo-fill" role="img" aria-label="Photo of a smiling older woman with white hair" style="background:radial-gradient(circle at 45% 40%,#e7e2dc,var(--photo-cool))"></div>
  </div>

  <div class="abs services">
    <h2 class="heading">Services</h2>
    <p class="tagline">One size does not fit all....</p>
    <div class="body-copy">
      <p>....especially when approaching brain health. The Thought Harbor approach starts by focusing on what you are noticing. Then we gather results from a variety of assessments, document targeted lab work and recommend specific life-style interventions. All of this is drawn together in a customized Renew Protocol® Road Map. At Thought Harbor we believe this is your journey and you need your Road Map.</p>
      <p>The human body is a complex machine. Often times multiple systems are affected that contribute to issues with cognition. This is why the current efforts of trying to find a singular drug to treat a multi system problem have been failing. At Thought Harbor we address the brain as part of a whole system, and our interventions reflect that.</p>
    </div>
  </div>
  <p class="abs back-url">www.thoughtharbor.org</p>

  <div class="abs revolution">
    <h2 class="heading">Health<br>Revolution!</h2>
    <ul class="checklist">
      <li>Enhance Brain Function</li>
      <li>Do not settle – Optimize your Brain at any age</li>
      <li>Prevent Cognitive Decline</li>
      <li>Reverse Early Dementia</li>
    </ul>
    <p class="strategies">Proven strategies can change<br>your life and destiny</p>
    <p class="slogan">Thought Harbor<br>-For Better Brain<br>Health-</p>
    <h3 class="contact-title">Contact Us</h3>
    <ul class="contact-list">
      <li><svg class="contact-icon" viewBox="0 0 26 26"><circle cx="13" cy="13" r="12" fill="none" stroke="var(--blue)" stroke-width="1.5"/><path d="M13 6a4.5 4.5 0 0 0-4.5 4.5c0 3.5 4.5 8.5 4.5 8.5s4.5-5 4.5-8.5A4.5 4.5 0 0 0 13 6z" fill="var(--blue)"/><circle cx="13" cy="10.5" r="1.6" fill="#fff"/></svg>Somewhere Lakeview, ND</li>
      <li><svg class="contact-icon" viewBox="0 0 26 26"><circle cx="13" cy="13" r="12" fill="none" stroke="var(--blue)" stroke-width="1.5"/><path d="M9 7l2.5-.5 1.5 3.5-1.8 1.2a8 8 0 0 0 3.6 3.6l1.2-1.8 3.5 1.5L19 17c-6 1-11-4-10-10z" fill="var(--blue)"/></svg>555-014-2390</li>
      <li><svg class="contact-icon" viewBox="0 0 26 26"><circle cx="13" cy="13" r="12" fill="none" stroke="var(--blue)" stroke-width="1.5"/><rect x="7" y="9" width="12" height="8" rx="1" fill="var(--blue)"/><path d="M7.5 9.5 13 14l5.5-4.5" stroke="#fff" stroke-width="1.2" fill="none"/></svg>info@thoughtharbor.com</li>
      <li><svg class="contact-icon" viewBox="0 0 26 26"><circle cx="13" cy="13" r="12" fill="none" stroke="var(--blue)" stroke-width="1.5"/><circle cx="13" cy="13" r="6" fill="none" stroke="var(--blue)" stroke-width="1.4"/><path d="M7 13h12M13 7c-2.5 3-2.5 9 0 12M13 7c2.5 3 2.5 9 0 12" stroke="var(--blue)" stroke-width="1.2" fill="none"/></svg>www.thoughtharbor.org</li>
    </ul>
  </div>

  <div class="brand brand--light" style="left:430px;top:775px;font-size:24px">
    <span class="brand-dot" style="width:22px;height:22px"></span>Thought Harbor
  </div>

  <div class="brand" style="left:800px;top:90px;font-size:24px">
    <span class="brand-dot" style="width:24px;height:24px"></span>Thought Harbor
  </div>
  <div class="photo" style="left:780px;top:160px;width:300px;height:300px">
    <div class="photo-fill" role="img" aria-label="Photo of a laughing grandfather carrying his granddaughter on his shoulders outdoors" style="background:radial-gradient(circle at 50% 45%,#e6c7b6,var(--photo-warm))"></div>
  </div>
  <h1 class="abs cover-title">Health<br>and<br>Wellbeing</h1>
  <p class="abs cover-pill">Treating Alzheimer's</p>
</section>

<section class="spread spread--inside">
  <svg class="spread-art" viewBox="0 0 1120 860" aria-hidden="true">
    <path d="M0 0 L400 0 C330 40 250 70 160 90 C90 105 40 130 0 160 Z" fill="var(--green)"/>
    <path d="M0 175 C60 120 150 100 230 88 C300 76 360 50 410 10" stroke="var(--blue)" stroke-width="8" fill="none"/>
    <path d="M1120 90 C1080 300 1020 500 940 640 C880 740 800 810 700 860 L1120 860 Z" fill="var(--green)"/>
    <path d="M900 570 C860 680 800 760 700 830" stroke="var(--blue)" stroke-width="10" fill="none"/>
    <path d="M930 600 C890 700 820 780 720 845" stroke="#fff" stroke-width="5" fill="none"/>
  </svg>

  <div class="photo" style="left:70px;top:130px;width:230px;height:230px">
    <div class="photo-fill" role="img" aria-label="Photo of a smiling older woman tending white flowers in a garden" style="background:radial-gradient(circle at 45% 35%,#e9d3c0,var(--photo-flower))"></div>
  </div>

  <div class="abs testimonials">
    <h2 class="heading">Testimonials</h2>
    <div class="quote">
      <p class="quote-name"><svg viewBox="0 0 24 24"><circle cx="12" cy="12" r="12" fill="var(--blue)"/><circle cx="12" cy="9.5" r="3.5" fill="#fff"/><path d="M5.5 18.5c1.2-3 3.6-4.5 6.5-4.5s5.3 1.5 6.5 4.5" fill="#fff"/></svg>Carol, Memory Care Alliance</p>
      <div class="body-copy">
        <p>Daniel is incredibly knowledgeable about what families face when managing dementia. His comprehensive experience shows when he provides information tailored to each unique individual.</p>
        <p>Daniel is an expert with taking research and bringing it to the level of being able to use the findings on a daily basis. I am so thankful for Daniel's passion for fighting Alzheimer's and dementia.</p>
      </div>
    </div>
    <div class="quote">
      <p class="quote-name"><svg viewBox="0 0 24 24"><circle cx="12" cy="12" r="12" fill="var(--blue)"/><circle cx="12" cy="9.5" r="3.5" fill="#fff"/><path d="M5.5 18.5c1.2-3 3.6-4.5 6.5-4.5s5.3 1.5 6.5 4.5" fill="#fff"/></svg>Joan, Previous Client</p>
      <div class="body-copy">
        <p>"Daniel has demonstrated time and time again his integrity, compassion, and expertise in the area of dementia and cognitive decline. His knowledge and experience has guided countless families through the difficult journey of dementia, and he has spent years advocating for the people behind the disease."</p>
      </div>
    </div>
  </div>

  <div class="abs approach">
    <h2 class="heading">Our<br>Approach</h2>
    <p class="sub">Your Brain Health Headquarters</p>
    <div class="body-copy">
      <p>Thought Harbor is your brain health headquarters. We are a resource you can turn to for the latest tools, therapeutic devices, guidance, programs, and insight necessary to protect and enhance your most important asset: YOUR BRAIN.</p>
      <p>Thought Harbor has partnered with Clear Path Minds located in Riverton, Idaho. All labs are reviewed, and the Renew Protocol® is collaboratively developed and reviewed by Clear Path Minds. Their expertise and ongoing research bring another layer of assurance and confidence to the process.</p>
      <p>According to the Memory Care Alliance, there are currently 6.2 million Americans living with Alzheimer's disease. That number is on target to triple between 2050 and 2060.</p>
      <p>By the time a person reaches 65 years of age, 2 out of 9 have Alzheimer's. In fact, latest research indicates that well over 10 years before the first symptoms appear (as Mild Cognitive Impairment) the disease is already at work in the brain. By the time a person reaches 85 over 32% will have Alzheimer's and that number is increasing.</p>
      <p>Present medications only manage symptoms or reduce existing Amyloid Plaque. New medications can cost as much as $52,000 a year, must be administered by IV and require monitoring through brain scans. The prevailing understanding has been that there is no cure, and Alzheimer's takes no hostages. All die!</p>
    </div>
  </div>

  <div class="abs team">
    <h2 class="heading">Meet<br>the Team</h2>
    <div class="member">
      <div class="member-photo" role="img" aria-label="Portrait photo of the founder"></div>
      <div><p class="member-name">Daniel Hartwell</p><p class="member-role">Founder of Thought Harbor</p></div>
    </div>
    <div class="member">
      <div class="member-photo" role="img" aria-label="Portrait photo of the principal and CEO"></div>
      <div><p class="member-name">Mark Ellison</p><p class="member-role">Principal &amp; CEO of Clear Path Minds®, LLC</p></div>
    </div>
    <div class="member">
      <div class="member-photo" role="img" aria-label="Portrait photo of the principal and CMO"></div>
      <div><p class="member-name">Peter Lindqvist</p><p class="member-role">NP-C, Principal &amp; CMO at Clear Path Minds®, LLC</p></div>
    </div>
  </div>

  <div class="brand brand--light" style="right:40px;top:755px;font-size:22px">
    <span class="brand-dot" style="width:20px;height:20px"></span>Thought Harbor
  </div>
  <p class="abs inside-url">www.thoughtharbor.org</p>
</section>

</body>
</html>
```